Honey Jar Label

I am looking for a logo for a 6oz. glass honey jar with a black lid that will contain honey from our bee boxes.
+ our product name is:  Meadow Lantern Honey
+ the label must include a Nutrition Facts label (google 'honey nutrition facts label' images for what to use).
+ dimensions:	 8 x 2.1875 inches (w x h)
+ color:	We can do one, two or three color prints. Use the VERILUX SHADE INDEX (VSI)
+ file types:  must be Adobe file (AI, PDF, PSD) or EPS files. We cannot accept other file types.
+ notes:	Gradients and halftones are strongly discouraged
+ provide all fonts with file or convert to outlines
+ design files must be CMYK, 300 dpi at 100%.

```html
<!DOCTYPE html>
<html lang="en">
<head>
<meta charset="utf-8">
<title>Meadow Lantern Honey – Jar Label</title>
<link rel="stylesheet" href="https://fonts.googleapis.com/css2?family=Arimo:wght@400;700&family=Sansita:wght@700&display=swap">
<style>
  :root {
    --honey-yellow: #fdb913;
    --label-black: #000000;
    --brand-orange: #f7a11a;
    --panel-white: #ffffff;
    --ink: #111111;
  }
  html, body {
    margin: 0;
    padding: 0;
    width: 1200px;
    height: 329px;
    overflow: hidden;
    background: var(--panel-white);
  }
  .label {
    position: relative;
    width: 1200px;
    height: 329px;
    overflow: hidden;
  }
  .comb-band {
    position: absolute;
    left: 0;
    width: 975px;
    background: var(--honey-yellow);
  }
  .comb-band--top { top: 0; height: 88px; }
  .comb-band--bottom { top: 240px; height: 89px; }
  .brand-band {
    position: absolute;
    left: 0;
    top: 88px;
    width: 975px;
    height: 152px;
    background: var(--label-black);
  }
  .brand-name {
    position: absolute;
    left: 390px;
    top: 8px;
    width: 220px;
    margin: 0;
    text-align: center;
    font-family: "Sansita", sans-serif;
    font-weight: 700;
    font-size: 40px;
    line-height: 44px;
    color: var(--brand-orange);
  }
  .brand-name span { display: block; }
  .nutrition {
    position: absolute;
    left: 975px;
    top: 0;
    width: 225px;
    height: 329px;
    background: var(--panel-white);
    font-family: "Arimo", sans-serif;
    color: var(--ink);
  }
  .nutrition__title {
    position: absolute;
    left: 6px;
    top: 2px;
    margin: 0;
    font-size: 17px;
    font-weight: 700;
  }
  .nutrition__serving {
    position: absolute;
    left: 8px;
    top: 27px;
    margin: 0;
    font-size: 13px;
    line-height: 17px;
  }
  .nutrition__dv-head {
    position: absolute;
    right: 7px;
    top: 63px;
    margin: 0;
    font-size: 13px;
  }
  .nutrition__rows {
    position: absolute;
    left: 8px;
    right: 7px;
    top: 80px;
    margin: 0;
    padding: 0;
    list-style: none;
    font-size: 13px;
    line-height: 16.8px;
  }
  .nutrition__row {
    display: flex;
    justify-content: space-between;
  }
  .nutrition__row--sub { padding-left: 16px; }
</style>
</head>
<body>
  <div class="label">
    <div class="comb-band comb-band--top" role="img" aria-label="Honeycomb pattern with a row of bees"></div>

    <div class="brand-band">
      <h1 class="brand-name"><span>Meadow</span><span>Lantern</span><span>Honey</span></h1>
    </div>

    <div class="comb-band comb-band--bottom" role="img" aria-label="Honeycomb pattern with a row of bees"></div>

    <section class="nutrition" aria-label="Nutrition Facts">
      <h2 class="nutrition__title">Nutrition Facts</h2>
      <p class="nutrition__serving">Amount Per-100g<br>Calories-304</p>
      <p class="nutrition__dv-head">%Daily Value</p>
      <ul class="nutrition__rows">
        <li class="nutrition__row"><span>Total fat-0g</span><span>0%</span></li>
        <li class="nutrition__row"><span>Saturated fat-0g</span><span>0%</span></li>
        <li class="nutrition__row"><span>Polyunsaturated fat-0g</span><span>0%</span></li>
        <li class="nutrition__row"><span>Monounsaturated fat-0g</span><span>0%</span></li>
        <li class="nutrition__row"><span>Cholesterol-0mg</span><span>0%</span></li>
        <li class="nutrition__row"><span>Sodium-4mg</span><span>0%</span></li>
        <li class="nutrition__row"><span>Potassium-52mg</span><span>1%</span></li>
        <li class="nutrition__row"><span>Total Carbohydrate-82g</span><span>27%</span></li>
        <li class="nutrition__row nutrition__row--sub"><span>Dietary fiber-0.2g</span><span>0%</span></li>
        <li class="nutrition__row nutrition__row--sub"><span>Sugar-82g</span><span></span></li>
        <li class="nutrition__row"><span>Protein-0.3g</span><span>0%</span></li>
        <li class="nutrition__row"><span>Vitamin A-0%</span><span>0%</span></li>
        <li class="nutrition__row"><span>Calcium &amp; Iron-0%</span><span>2%</span></li>
        <li class="nutrition__row"><span>Vitamin B-6-0%</span><span>0%</span></li>
        <li class="nutrition__row"><span>Magnesium-0%</span><span></span></li>
      </ul>
    </section>
  </div>
</body>
</html>
```